Brightwire electrical flyer for distribution to get more clients

I need to make a flyer to distribute to the local neighbourhood. we are an electrical company and the name is Brightwire electrical contractors. the website is www.brightwire-electrical-example.ca We do custom homes, knob and tube home re-wires, fuse to breaker panel upgrades, service upgrades 100 amp and 200 amp, pot lights, roof de-icing cables, floor heat cables, pot lights, surge protection, smoke detectors. Flyer size is half page 216mm X 139mm

Target Market(s)

home owners

Industry/Entity Type

Electrician

Font styles to use
Sans Serif

Requirements
Must have
• flyer must list our services and geared more toward the knob and tube replacement. must have company name and number 416-555-3928 and our OSB/PCRA licence number which is 4829350
Nice to have
• try to match the colour scheme of the website with the flyer www.brightwire-electrical-example.ca

```html
<!DOCTYPE html>
<html lang="en">
<head>
<meta charset="utf-8">
<title>Brightwire Electrical Contractors – Flyer</title>
<link rel="stylesheet" href="https://fonts.googleapis.com/css2?family=Open+Sans:wght@700;800&family=Source+Sans+3:wght@400;600;700&display=swap">
<style>
  :root {
    --charcoal: #353535;
    --yellow: #fcc817;
    --gold: #d6ac16;
    --orange: #f7941d;
    --white: #ffffff;
    --grey-text: #8a8a8a;
    --body-text: #e6e6e6;
    --page: #e8e6e3;
    --ink: #1e1e1e;
  }
  * { margin: 0; padding: 0; box-sizing: border-box; }
  html, body { width: 1001px; height: 1200px; overflow: hidden; }
  body {
    background: var(--page);
    position: relative;
    font-family: "Source Sans 3", sans-serif;
  }
  .card {
    position: absolute;
    width: 778px;
    height: 512px;
    background: var(--charcoal);
    overflow: hidden;
    box-shadow: 0 3px 10px rgba(0,0,0,0.25);
  }
  .card-front { left: 96px; top: 50px; }
  .card-back { left: 178px; top: 610px; }
  .card-shapes { position: absolute; inset: 0; }

  /* front */
  .brand {
    position: absolute;
    color: var(--yellow);
    font-family: "Source Sans 3", sans-serif;
    font-weight: 600;
    display: flex;
    align-items: center;
    gap: 10px;
  }
  .brand-dot {
    width: 22px; height: 22px; border-radius: 50%;
    background: var(--yellow); flex: none;
  }
  .brand-text { line-height: 1; }
  .brand-name { display: block; text-transform: uppercase; }
  .brand-sub { display: block; }
  .card-front .brand { right: 20px; top: 92px; text-align: right; }
  .card-front .brand-name { font-size: 40px; letter-spacing: 4px; }
  .card-front .brand-sub { font-size: 19px; letter-spacing: 1.2px; margin-top: 6px; }
  .licence {
    position: absolute; right: 20px; top: 173px;
    color: var(--grey-text); font-size: 12px;
  }
  .about {
    position: absolute; right: 20px; width: 260px;
    color: var(--body-text); font-size: 11.5px; line-height: 15px; text-align: right;
  }
  .about-intro { top: 230px; }
  .about-services { top: 305px; width: 230px; }
  .badge-shape {
    position: absolute; border-radius: 50%; background: var(--orange);
  }
  .card-front .badge-shape { left: 612px; top: 424px; width: 68px; height: 68px; }
  .front-phone {
    position: absolute; left: 30px; top: 442px;
    font-family: "Open Sans", sans-serif; font-weight: 800;
    font-size: 38px; color: var(--ink); letter-spacing: -0.5px;
  }
  .front-web {
    position: absolute; left: 31px; top: 487px;
    font-family: "Open Sans", sans-serif; font-weight: 700;
    font-size: 13px; letter-spacing: 0.6px; color: var(--ink);
  }

  /* back */
  .card-back .brand { left: 22px; top: 40px; }
  .card-back .brand-name { font-size: 34px; letter-spacing: 4px; }
  .card-back .brand-sub { font-size: 15px; letter-spacing: 1px; margin-top: 5px; }
  .call-label {
    position: absolute; right: 18px; top: 24px;
    color: var(--white); font-weight: 700; font-size: 17px; letter-spacing: -0.2px;
  }
  .call-phone {
    position: absolute; right: 18px; top: 44px;
    color: var(--white); font-family: "Open Sans", sans-serif; font-weight: 700;
    font-size: 38px; letter-spacing: -0.5px;
  }
  .services-banner {
    position: absolute; left: 0; top: 143px; width: 506px; height: 35px;
    background: var(--gold); border-radius: 0 18px 18px 0;
    color: var(--white); font-weight: 700; font-size: 20px;
    line-height: 35px; padding-left: 25px; letter-spacing: -0.2px;
  }
  .service-list {
    position: absolute; left: 0; top: 196px; width: 778px; list-style: none;
  }
  .service {
    position: absolute; display: flex; align-items: center; gap: 9px;
    color: var(--white); font-size: 22px; white-space: nowrap;
  }
  .service-icon { width: 19px; height: 19px; flex: none; }
  .card-back .badge-shape { left: 29px; top: 340px; width: 70px; height: 70px; }
  .service-photo {
    position: absolute; border-radius: 50%; border: 4px solid var(--white);
    box-shadow: 0 2px 6px rgba(0,0,0,0.35);
  }
  .photo-detector { left: 362px; top: 354px; width: 104px; height: 104px;
    background: radial-gradient(circle at 45% 45%, #ffffff, #d9dadc 60%, #b7b9bc); }
  .photo-wiring { left: 488px; top: 336px; width: 116px; height: 116px;
    background: radial-gradient(circle at 50% 45%, #b98a66, #8a5a3a 65%, #5e3b24); }
  .photo-roof { left: 631px; top: 314px; width: 128px; height: 128px;
    background: linear-gradient(160deg, #cfd4da, #f4f5f7 45%, #6b5a52 80%, #3b3330); }
  .contact-row {
    position: absolute; left: 22px; right: 18px; top: 462px;
    display: flex; justify-content: space-between; align-items: center;
    color: var(--ink); font-size: 16.5px;
  }
  .contact-item { display: flex; align-items: center; gap: 7px; white-space: nowrap; }
  .contact-icon { width: 18px; height: 18px; flex: none; }
</style>
</head>
<body>

<section class="card card-front" aria-label="Flyer front">
  <svg class="card-shapes" viewBox="0 0 778 512" width="778" height="512">
    <polygon points="0,0 400,0 590,512 0,512" fill="#cfc9c0" role="img"
      aria-label="Photo of a bright modern kitchen with white island, bar stools and wood floor"/>
    <polygon points="0,0 400,0 590,512 0,512" fill="url(#kitchenTone)" />
    <line x1="400" y1="0" x2="590" y2="512" stroke="#ffffff" stroke-width="6"/>
    <polygon points="408,130 434,130 632,512 598,512" fill="#fcc817"/>
    <polygon points="0,364 48,364 36,398 0,500" fill="#353535"/>
    <polygon points="40,398 304,398 352,512 0,512 0,500" fill="#fcc817"/>
    <defs>
      <linearGradient id="kitchenTone" x1="0" y1="0" x2="0" y2="1">
        <stop offset="0" stop-color="#f2f2f0" stop-opacity="0.85"/>
        <stop offset="0.55" stop-color="#dcdad6" stop-opacity="0.5"/>
        <stop offset="1" stop-color="#b88a5e" stop-opacity="0.9"/>
      </linearGradient>
    </defs>
  </svg>

  <div class="brand">
    <span class="brand-dot"></span>
    <span class="brand-text">
      <span class="brand-name">Brightwire</span>
      <span class="brand-sub">Electrical Contractors Inc.</span>
    </span>
  </div>
  <p class="licence">OSB/PCRA 4829350</p>
  <p class="about about-intro">We are licenced electrical contractors based out of Toronto and serving all of the GTA. We specialize in custom homes and knob and tube removal. We are fully licenced and insured.</p>
  <p class="about about-services">We offer a wide variety of services. From custom homes to home re-wires and renovations we can do it all.</p>
  <div class="badge-shape" role="img" aria-label="Safety authority certification badge"></div>

  <p class="front-phone">416-555-3928</p>
  <p class="front-web">www.brightwire-electrical-example.ca</p>
</section>

<section class="card card-back" aria-label="Flyer back">
  <svg class="card-shapes" viewBox="0 0 778 512" width="778" height="512">
    <polygon points="0,437 778,360 778,512 0,512" fill="#fcc817"/>
    <line x1="0" y1="433" x2="778" y2="356" stroke="#ffffff" stroke-width="7"/>
  </svg>

  <div class="brand">
    <span class="brand-dot"></span>
    <span class="brand-text">
      <span class="brand-name">Brightwire</span>
      <span class="brand-sub">Electrical Contractors Inc.</span>
    </span>
  </div>
  <p class="call-label">CALL US TODAY</p>
  <p class="call-phone">416-555-3928</p>

  <h2 class="services-banner">WE OFFER A WIDE VARIETY OF SERVICES</h2>

  <ul class="service-list">
    <li class="service" style="left:29px;top:0">
      <svg class="service-icon" viewBox="0 0 20 20"><circle cx="10" cy="10" r="10" fill="#fcc817"/><path d="M8 5.5 12.5 10 8 14.5" fill="none" stroke="#353535" stroke-width="2.6"/></svg>Custom homes</li>
    <li class="service" style="left:29px;top:37px">
      <svg class="service-icon" viewBox="0 0 20 20"><circle cx="10" cy="10" r="10" fill="#fcc817"/><path d="M8 5.5 12.5 10 8 14.5" fill="none" stroke="#353535" stroke-width="2.6"/></svg>Surge protection</li>
    <li class="service" style="left:29px;top:74px">
      <svg class="service-icon" viewBox="0 0 20 20"><circle cx="10" cy="10" r="10" fill="#fcc817"/><path d="M8 5.5 12.5 10 8 14.5" fill="none" stroke="#353535" stroke-width="2.6"/></svg>Electrical solutions</li>
    <li class="service" style="left:239px;top:0">
      <svg class="service-icon" viewBox="0 0 20 20"><circle cx="10" cy="10" r="10" fill="#fcc817"/><path d="M8 5.5 12.5 10 8 14.5" fill="none" stroke="#353535" stroke-width="2.6"/></svg>Pot lights</li>
    <li class="service" style="left:239px;top:37px">
      <svg class="service-icon" viewBox="0 0 20 20"><circle cx="10" cy="10" r="10" fill="#fcc817"/><path d="M8 5.5 12.5 10 8 14.5" fill="none" stroke="#353535" stroke-width="2.6"/></svg>Knob and tube re-wiring</li>
    <li class="service" style="left:239px;top:74px">
      <svg class="service-icon" viewBox="0 0 20 20"><circle cx="10" cy="10" r="10" fill="#fcc817"/><path d="M8 5.5 12.5 10 8 14.5" fill="none" stroke="#353535" stroke-width="2.6"/></svg>Fuse to breaker upgrade</li>
    <li class="service" style="left:515px;top:0">
      <svg class="service-icon" viewBox="0 0 20 20"><circle cx="10" cy="10" r="10" fill="#fcc817"/><path d="M8 5.5 12.5 10 8 14.5" fill="none" stroke="#353535" stroke-width="2.6"/></svg>Service upgrade</li>
    <li class="service" style="left:515px;top:37px">
      <svg class="service-icon" viewBox="0 0 20 20"><circle cx="10" cy="10" r="10" fill="#fcc817"/><path d="M8 5.5 12.5 10 8 14.5" fill="none" stroke="#353535" stroke-width="2.6"/></svg>Smoke detectors</li>
    <li class="service" style="left:515px;top:74px">
      <svg class="service-icon" viewBox="0 0 20 20"><circle cx="10" cy="10" r="10" fill="#fcc817"/><path d="M8 5.5 12.5 10 8 14.5" fill="none" stroke="#353535" stroke-width="2.6"/></svg>Roof and floor heating</li>
  </ul>

  <div class="badge-shape" role="img" aria-label="Safety authority certification badge"></div>

  <div class="service-photo photo-detector" role="img" aria-label="Photo of a white ceiling smoke detector"></div>
  <div class="service-photo photo-wiring" role="img" aria-label="Photo of old knob and tube wiring between wooden joists"></div>
  <div class="service-photo photo-roof" role="img" aria-label="Photo of de-icing heat cables on a snowy roof edge"></div>

  <div class="contact-row">
    <span class="contact-item">
      <svg class="contact-icon" viewBox="0 0 20 20"><circle cx="10" cy="10" r="8.5" fill="none" stroke="#1e1e1e" stroke-width="1.6"/><circle cx="10" cy="10" r="3" fill="none" stroke="#1e1e1e" stroke-width="1.6"/><path d="M13 7v4.5a1.8 1.8 0 0 0 3.6 0" fill="none" stroke="#1e1e1e" stroke-width="1.6"/></svg>
      sam@brightwire-electrical-example.ca</span>
    <span class="contact-item">
      <svg class="contact-icon" viewBox="0 0 20 20"><circle cx="10" cy="10" r="8.5" fill="none" stroke="#1e1e1e" stroke-width="1.6"/><path d="M6.5 5.5l2 -.5 1.2 2.6-1.3 1a6 6 0 0 0 3 3l1-1.3 2.6 1.2-.5 2c-4.5.4-8.4-3.5-8-8z" fill="#1e1e1e"/></svg>
      416-555-3928</span>
    <span class="contact-item">
      <svg class="contact-icon" viewBox="0 0 20 20"><circle cx="10" cy="10" r="8.5" fill="none" stroke="#1e1e1e" stroke-width="1.6"/><rect x="9.1" y="8.5" width="1.8" height="6" fill="#1e1e1e"/><circle cx="10" cy="6" r="1.1" fill="#1e1e1e"/></svg>
      www.brightwire-electrical-example.ca</span>
  </div>
</section>

</body>
</html>
```